Flyer Design with BIO and company detail

Ideally I would like a DL size Flyer that has my personal bio and photo on one side and the company logo as per the attached file - half page add on the back

Industry/Entity Type

It Company

```html
<!DOCTYPE html>
<html lang="en">
<head>
<meta charset="utf-8">
<title>Kestrel Financial – DL Flyer</title>
<link rel="stylesheet" href="https://fonts.googleapis.com/css2?family=Cormorant+Garamond:wght@500&family=Open+Sans:wght@400;600&family=Roboto+Condensed:wght@400;700&display=swap">
<style>
  :root {
    --bg: #e9eaee;
    --navy: #0d1d5a;
    --royal: #1f3fa3;
    --bright: #2d5fd0;
    --sky: #4f86e8;
    --ink: #2a2f3d;
    --muted: #6b7080;
    --rule: #d5d8e0;
    --white: #ffffff;
    --photo-a: #cfc7bd;
    --photo-b: #8f8476;
  }
  * { margin: 0; padding: 0; box-sizing: border-box; }
  html, body { width: 900px; height: 1200px; overflow: hidden; background: var(--bg); }
  body { position: relative; font-family: "Open Sans", sans-serif; }

  .card {
    position: absolute; left: 40px; width: 820px; height: 390px;
    overflow: hidden; box-shadow: 0 6px 18px rgba(13, 29, 90, 0.18);
  }

  /* Front */
  .card--front { top: 180px; background: linear-gradient(100deg, var(--navy) 0%, var(--royal) 45%, var(--bright) 100%); }
  .front__pattern {
    position: absolute; left: 0; top: 0; width: 300px; height: 390px;
    background: radial-gradient(ellipse at 20% 50%, rgba(79, 134, 232, 0.55), rgba(79, 134, 232, 0) 70%);
  }
  .front__logo {
    position: absolute; left: 360px; top: 148px;
    font-family: "Cormorant Garamond", serif; font-weight: 500;
    font-size: 62px; line-height: 1; color: var(--white); letter-spacing: 0.5px;
  }

  /* Back */
  .card--back { top: 630px; background: var(--white); }
  .back__art { position: absolute; left: 0; top: 0; }
  .back__header {
    position: absolute; left: 320px; right: 0; top: 12px; height: 28px;
    background: linear-gradient(90deg, var(--royal), var(--navy));
    color: var(--white); font-family: "Roboto Condensed", sans-serif;
    font-size: 15px; letter-spacing: 1px; text-align: right;
    padding-right: 22px; line-height: 28px; text-transform: uppercase;
  }
  .bio {
    position: absolute; left: 322px; right: 22px; top: 52px;
    font-size: 10px; line-height: 1.4; color: var(--ink); text-align: right;
  }
  .bio p + p { margin-top: 6px; }
  .services {
    position: absolute; left: 330px; right: 0; top: 264px; height: 50px;
    background: linear-gradient(90deg, var(--royal), var(--navy));
    display: flex; justify-content: flex-end; gap: 34px; padding: 7px 26px 0 0;
    color: var(--white); font-size: 12px; line-height: 18px;
  }
  .services__col--left { text-align: right; }
  .services__item { display: flex; align-items: center; gap: 7px; }
  .services__col--left .services__item { justify-content: flex-end; }
  .services__mark { width: 6px; height: 6px; background: var(--sky); display: inline-block; }
  .contact {
    position: absolute; left: 300px; right: 22px; top: 338px; height: 34px;
    border-top: 1px solid var(--rule);
    display: flex; justify-content: space-between; align-items: center;
    font-size: 9px; color: var(--muted);
  }
  .contact__item { display: flex; align-items: center; gap: 5px; }
  .contact__item svg { width: 10px; height: 10px; fill: var(--royal); }
</style>
</head>
<body>

<section class="card card--front">
  <div class="front__pattern" role="img" aria-label="Decorative field of blue dots fading toward the centre"></div>
  <div class="front__logo">kestrel financial</div>
</section>

<section class="card card--back">
  <svg class="back__art" width="820" height="390" viewBox="0 0 820 390">
    <defs>
      <linearGradient id="photoTone" x1="0" y1="0" x2="0" y2="1">
        <stop offset="0" stop-color="var(--photo-a)"/>
        <stop offset="1" stop-color="var(--photo-b)"/>
      </linearGradient>
    </defs>
    <circle cx="150" cy="180" r="128" fill="url(#photoTone)" role="img" aria-label="Portrait photograph of Danielle Harper"/>
    <path d="M150 30 A150 150 0 0 1 250 292 Q290 312 340 296" fill="none" stroke="var(--royal)" stroke-width="13"/>
    <path d="M150 16 A164 164 0 0 1 259 302 Q300 320 340 310" fill="none" stroke="var(--sky)" stroke-width="3"/>
    <path d="M0 312 Q120 338 280 318" fill="none" stroke="var(--navy)" stroke-width="9"/>
  </svg>

  <div class="back__header">Danielle Harper – Bio</div>

  <div class="bio">
    <p>Danielle Harper is a director and Senior Financial Adviser with Kestrel Financial Pty Ltd. With over 25 years' experience in financial management, taxation and business. In addition Danielle has extensive experience with complex structures including Self Managed Super Funds, Family Trusts, Companies, Individual Investors and Asset Protection.</p>
    <p>Danielle is a Fellow of the Practising Accountants Institute, holds a Bachelor of Business (ACC), Graduate Diploma of Financial Planning, and is an accredited Self Managed Super Fund (SMSF) Specialist.</p>
    <p>With this experience Danielle is able to give clients comprehensive financial advice, taking an holistic approach that considers your goals and objectives and the most effective way to achieve them in today's environment.</p>
    <p>Danielle is an Authorised Representative of Northgate Wealth Limited (AFSL 318742) and is licensed to provide financial planning services which include advising and dealing in the following:</p>
  </div>

  <div class="services">
    <div class="services__col services__col--left">
      <div class="services__item">Managed Investments <span class="services__mark"></span></div>
      <div class="services__item">Superannuation and Retirement Planning <span class="services__mark"></span></div>
    </div>
    <div class="services__col">
      <div class="services__item"><span class="services__mark"></span> Financial Planning</div>
      <div class="services__item"><span class="services__mark"></span> Risk Management</div>
    </div>
  </div>

  <div class="contact">
    <span class="contact__item">
      <svg viewBox="0 0 10 10"><circle cx="5" cy="5" r="4.5"/></svg>kestrelfinancial.example
    </span>
    <span class="contact__item">
      <svg viewBox="0 0 10 10"><path d="M5 0a3.5 3.5 0 0 0-3.5 3.5C1.5 6 5 10 5 10s3.5-4 3.5-6.5A3.5 3.5 0 0 0 5 0zm0 5a1.5 1.5 0 1 1 0-3 1.5 1.5 0 0 1 0 3z"/></svg>Level 2, 48 Harbour Road, Brookvale QLD 4001
    </span>
    <span class="contact__item">
      <svg viewBox="0 0 10 10"><path d="M2 0.5l2 2-1 1.3a6 6 0 0 0 3.2 3.2l1.3-1 2 2-1.2 1.5C5 9.5 0.5 5 0.5 1.7z"/></svg>(07) 5550 1842
    </span>
  </div>
</section>

</body>
</html>
```